Card Design to Advertise New Business

I am looking to have a card designed so that I can pass it out to help promote my business. I have never done this before so I honestly do not know where to start with any ideas. I am providing my website address to help. I provide math tutoring, test prep, and schooling options.

I am looking for a card bigger than a business card but smaller than a flyer. Something front and back that I can pass out.

Business Information
Phone: 470-555-0192
Website: www.kelvanostudyhall.example
Address: 418 Brackenfield Rd Ste 340 Larkmoor OH 43218
Email: kelvanoservices@kelvanomail.example

Services:
Math Tutoring
NEQ & BOW Test Prep
Group and Private Sessions
Fully Accredited Private School

Target Market(s)

Middle and High School Students

Industry/Entity Type

Education

Requirements
Must have
• Information from my website

```html
<!DOCTYPE html>
<html lang="en">
<head>
<meta charset="utf-8">
<title>Kelvano Study Hall – Postcard</title>
<link href="https://fonts.googleapis.com/css2?family=Oswald:wght@500;600&family=Roboto:wght@400;500;700&family=Dancing+Script:wght@700&display=swap" rel="stylesheet">
<style>
  :root{
    --stage:#000000;
    --white:#ffffff;
    --blue:#3c5fb5;
    --box:#1f3f95;
    --navy:#14286a;
    --red:#c1341f;
    --green:#22c02a;
    --purple:#7b56c0;
    --yellow:#f4e23a;
    --ink:#333333;
    --brand:#2a56a8;
  }
  *{margin:0;padding:0;box-sizing:border-box}
  html,body{width:1200px;height:1177px;overflow:hidden;background:var(--stage)}
  body{position:relative;font-family:"Roboto",Arial,sans-serif}
  .card{position:absolute;background:var(--white);overflow:hidden}
  .card svg.art{position:absolute;left:0;top:0}
  .abs{position:absolute}

  /* front */
  .card--front{left:349px;top:101px;width:704px;height:468px}
  .brand{position:absolute;text-align:center;font-family:"Oswald",sans-serif;font-weight:600;color:var(--brand);letter-spacing:.5px;white-space:nowrap;line-height:1.2}
  .brand-dot{border-radius:50%;background:var(--brand);position:absolute}
  .front-dot{left:70px;top:164px;width:94px;height:94px}
  .front-brand{left:0;width:238px;top:264px;font-size:20px}
  .goal{left:25px;top:311px;width:172px;font-size:12.6px;line-height:15.2px;color:var(--ink);text-align:justify}
  .services-tab{left:219px;top:273px;width:27px;height:122px;background:var(--green);border-radius:6px 0 0 6px;display:flex;align-items:center;justify-content:center}
  .services-tab span{writing-mode:vertical-rl;transform:rotate(180deg);color:var(--white);font-weight:700;font-size:13px;letter-spacing:3.5px}
  .headline{left:246px;width:458px;top:192px;text-align:center;font-family:"Oswald",sans-serif;font-weight:600;color:var(--white);font-size:27px;line-height:1.2;letter-spacing:.2px;white-space:nowrap}
  .tagline{left:246px;width:458px;top:229px;text-align:center;font-family:"Dancing Script",cursive;color:var(--yellow);font-size:19px;line-height:1.2}
  .service{top:270px;width:93px;height:127px;background:var(--box);border:2px solid var(--white);border-radius:10px;display:flex;flex-direction:column;align-items:center;padding-top:13px}
  .service svg{width:42px;height:42px}
  .service p{margin-top:9px;color:var(--white);font-size:10px;font-weight:700;line-height:12px;text-align:center}
  .credit{left:246px;width:458px;top:403px;text-align:center;color:#dfe6fa;font-size:6.5px}
  .phone{display:flex;align-items:center;justify-content:center;gap:9px;color:var(--white);font-family:"Oswald",sans-serif;font-weight:500;font-size:25px}
  .phone svg{width:24px;height:24px}
  .front-phone{left:0;top:425px;width:246px;height:43px}
  .contact{display:flex;gap:6px;color:var(--white);font-size:11px;line-height:13px;white-space:nowrap}
  .contact svg{width:9px;height:11px;flex:none;margin-top:1px}
  .contact b{font-weight:700}
  .contact .hl{color:var(--yellow)}

  /* back */
  .card--back{left:132px;top:614px;width:708px;height:473px}
  .name-tab{left:0;top:102px;width:64px;height:303px;background:var(--purple);border:2px solid var(--white);border-left:none;border-radius:0 10px 10px 0;display:flex;align-items:center;justify-content:center}
  .name-tab span{writing-mode:vertical-rl;transform:rotate(180deg);font-family:"Oswald",sans-serif;font-weight:600;font-size:36px;color:var(--white);letter-spacing:.5px;white-space:nowrap}
  .name-tab em{font-style:normal;color:var(--yellow)}
  .bio{left:76px;top:114px;width:228px;color:var(--white);font-size:12.4px;line-height:15.1px}
  .bio p+p{margin-top:15.1px}
  .stamp{left:602px;top:20px;width:83px;height:97px;border:1px solid #9a9a9a}
  .back-dot{left:549px;top:280px;width:94px;height:94px}
  .back-brand{left:479px;width:234px;top:382px;font-size:21px}
  .back-phone{left:462px;top:421px;width:246px;height:52px}
</style>
</head>
<body>

<!-- FRONT -->
<section class="card card--front">
  <svg class="art" width="704" height="468" viewBox="0 0 704 468">
    <defs>
      <linearGradient id="photoA" x1="0" y1="0" x2="1" y2="1"><stop offset="0" stop-color="#c44a3c"/><stop offset=".5" stop-color="#e3b49a"/><stop offset="1" stop-color="#f2ece6"/></linearGradient>
      <linearGradient id="photoB" x1="0" y1="0" x2="1" y2="1"><stop offset="0" stop-color="#6f8fc9"/><stop offset=".5" stop-color="#e2c2a2"/><stop offset="1" stop-color="#b9cbe6"/></linearGradient>
      <linearGradient id="photoC" x1="0" y1="0" x2="1" y2="1"><stop offset="0" stop-color="#d6d6d4"/><stop offset=".6" stop-color="#c8a290"/><stop offset="1" stop-color="#cfcfcd"/></linearGradient>
    </defs>
    <path d="M0,0 H238 V140 Q120,126 0,152 Z" fill="url(#photoA)" role="img" aria-label="Photo: young children writing in workbooks"/>
    <rect x="246" y="0" width="256" height="175" fill="url(#photoB)" role="img" aria-label="Photo: smiling students working together at a desk"/>
    <rect x="508" y="0" width="196" height="175" fill="url(#photoC)" role="img" aria-label="Photo: student holding books in front of a board of equations"/>
    <path d="M246,166 Q500,160 704,112 V124 Q500,172 246,178 Z" fill="var(--white)"/>
    <path d="M246,178 Q500,172 704,124 V425 H246 Z" fill="var(--blue)"/>
    <rect x="0" y="425" width="246" height="43" fill="var(--red)"/>
    <rect x="246" y="425" width="458" height="43" fill="var(--navy)"/>
  </svg>

  <div class="brand-dot front-dot"></div>
  <div class="brand front-brand">KELVANO STUDY HALL</div>
  <p class="abs goal">Our goal is to not only build math competency but build self-confidence to perform better in classes &amp; tests and any other goals you choose to take on in life.</p>
  <div class="abs services-tab"><span>SERVICES</span></div>

  <h1 class="abs headline">SKILL COACHING &amp; MATH TUTORING</h1>
  <p class="abs tagline">For All Ages</p>

  <div class="abs service" style="left:277px">
    <svg viewBox="0 0 42 42" fill="none" stroke="#fff" stroke-width="2"><rect x="5" y="3" width="32" height="36" rx="3"/><line x1="21" y1="3" x2="21" y2="39"/><line x1="5" y1="21" x2="37" y2="21"/><path d="M13 8v8M9 12h8M25 12h8M10 26l6 6M16 26l-6 6M25 28h8M25 32h8"/></svg>
    <p>MATH<br>TUTORING</p>
  </div>
  <div class="abs service" style="left:381px">
    <svg viewBox="0 0 42 42" fill="none" stroke="#fff" stroke-width="2"><rect x="6" y="3" width="26" height="36" rx="2"/><path d="M10 9h14M10 16l2 2 3-4M18 16h10M10 24l2 2 3-4M18 24h10M10 32h14"/><path d="M38 10l-8 20-2 5 1-5 8-20z"/></svg>
    <p>NEQ &amp; BOW<br>TEST PREP</p>
  </div>
  <div class="abs service" style="left:485px">
    <svg viewBox="0 0 42 42" fill="none" stroke="#fff" stroke-width="2"><circle cx="9" cy="14" r="3.5"/><circle cx="17" cy="12" r="3.5"/><circle cx="25" cy="14" r="3.5"/><path d="M3 30v-6a5 5 0 0 1 10 0M11 30v-8a6 6 0 0 1 12 0v8M19 30v-6a5 5 0 0 1 10 0v6M2 30h28"/><circle cx="36" cy="14" r="3.5"/><path d="M31 30v-7a5 5 0 0 1 10 0v7z"/></svg>
    <p>GROUP AND<br>PRIVATE<br>SESSIONS</p>
  </div>
  <div class="abs service" style="left:589px">
    <svg viewBox="0 0 42 42" fill="none" stroke="#fff" stroke-width="2"><circle cx="21" cy="16" r="12"/><circle cx="21" cy="16" r="8"/><path d="M21 11l1.6 3.3 3.6.4-2.7 2.4.8 3.5-3.3-1.9-3.3 1.9.8-3.5-2.7-2.4 3.6-.4z"/><path d="M14 26l-4 12 5-2 3 4 3-10M28 26l4 12-5-2-3 4-3-10"/></svg>
    <p>FULLY<br>ACCREDITED<br>PRIVATE<br>SCHOOL</p>
  </div>
  <p class="abs credit">Icon set credits listed on our website</p>

  <div class="abs phone front-phone">
    <svg viewBox="0 0 24 24"><circle cx="12" cy="12" r="11" fill="#fff"/><path d="M8.2 6.5l2 2.2-1 1.6c.7 1.6 2 2.9 3.6 3.6l1.6-1 2.2 2-1.2 2c-4.2-.4-8.4-4.6-8.8-8.8z" fill="var(--red)"/></svg>
    <span>470-555-0192</span>
  </div>
  <div class="abs contact" style="left:268px;top:432px">
    <svg viewBox="0 0 9 11"><path d="M4.5 0A4 4 0 0 0 .5 4c0 3 4 7 4 7s4-4 4-7a4 4 0 0 0-4-4zm0 5.6A1.6 1.6 0 1 1 4.5 2.4a1.6 1.6 0 0 1 0 3.2z" fill="var(--yellow)"/></svg>
    <span>418 Brackenfield Rd Ste 340<br>Larkmoor OH 43218</span>
  </div>
  <div class="abs contact" style="left:467px;top:432px">
    <svg viewBox="0 0 9 11"><rect x="0" y="2" width="9" height="7" rx="1" fill="var(--yellow)"/><path d="M0.5 2.5l4 3 4-3" stroke="var(--navy)" fill="none"/></svg>
    <span>kelvanoservices@kelvanomail.example</span>
  </div>
  <div class="abs contact" style="left:467px;top:446px">
    <svg viewBox="0 0 9 11"><circle cx="4.5" cy="5.5" r="4" fill="var(--yellow)"/><path d="M.5 5.5h8M4.5 1.5c-2 2.5-2 5.5 0 8M4.5 1.5c2 2.5 2 5.5 0 8" stroke="var(--navy)" stroke-width=".7" fill="none"/></svg>
    <b>www.<span class="hl">kelvanostudyhall.example</span></b>
  </div>
</section>

<!-- BACK -->
<section class="card card--back">
  <svg class="art" width="708" height="473" viewBox="0 0 708 473">
    <defs>
      <clipPath id="aboveFooter"><rect x="0" y="0" width="708" height="421"/></clipPath>
      <linearGradient id="portrait" x1="0" y1="0" x2="0" y2="1"><stop offset="0" stop-color="#6b4a3a"/><stop offset=".45" stop-color="#9a6a50"/><stop offset="1" stop-color="#7fb3d6"/></linearGradient>
    </defs>
    <circle cx="136" cy="346" r="329" fill="var(--green)" clip-path="url(#aboveFooter)"/>
    <path d="M304,421 V290 Q304,228 373,228 Q442,228 442,290 V421 Z" fill="url(#portrait)" role="img" aria-label="Portrait photo of the lead math instructor"/>
    <rect x="0" y="421" width="462" height="52" fill="var(--navy)"/>
    <rect x="462" y="421" width="246" height="52" fill="var(--red)"/>
  </svg>

  <div class="abs name-tab"><span>MARISOL <em>TENNEY</em></span></div>
  <div class="abs bio">
    <p>Marisol has 14 years of classroom experience as a 6-12 gifted mathematics teacher, paraprofessional educator, substitute teacher, and college instructor. Currently, Marisol is the lead mathematics instructor at a local college where she teaches a variety of math courses in face-to-face, hybrid, and online formats.</p>
    <p>She also has experience as a math consultant for a major textbook company. She holds a Bachelor of Business Administration from Harwell State University where she majored in actuarial science. And a Master of Arts in Teaching from Harwell State University where she majored in Mathematics Education.</p>
  </div>

  <div class="abs stamp"></div>
  <div class="brand-dot back-dot"></div>
  <div class="brand back-brand">KELVANO STUDY HALL</div>

  <div class="abs contact" style="left:16px;top:432px">
    <svg viewBox="0 0 9 11"><path d="M4.5 0A4 4 0 0 0 .5 4c0 3 4 7 4 7s4-4 4-7a4 4 0 0 0-4-4zm0 5.6A1.6 1.6 0 1 1 4.5 2.4a1.6 1.6 0 0 1 0 3.2z" fill="var(--yellow)"/></svg>
    <span>418 Brackenfield Rd Ste 340<br>Larkmoor OH 43218</span>
  </div>
  <div class="abs contact" style="left:216px;top:432px">
    <svg viewBox="0 0 9 11"><rect x="0" y="2" width="9" height="7" rx="1" fill="var(--yellow)"/><path d="M0.5 2.5l4 3 4-3" stroke="var(--navy)" fill="none"/></svg>
    <span>kelvanoservices@kelvanomail.example</span>
  </div>
  <div class="abs contact" style="left:216px;top:446px">
    <svg viewBox="0 0 9 11"><circle cx="4.5" cy="5.5" r="4" fill="var(--yellow)"/><path d="M.5 5.5h8M4.5 1.5c-2 2.5-2 5.5 0 8M4.5 1.5c2 2.5 2 5.5 0 8" stroke="var(--navy)" stroke-width=".7" fill="none"/></svg>
    <b>www.kelvanostudyhall.example</b>
  </div>
  <div class="abs phone back-phone">
    <svg viewBox="0 0 24 24"><circle cx="12" cy="12" r="11" fill="#fff"/><path d="M8.2 6.5l2 2.2-1 1.6c.7 1.6 2 2.9 3.6 3.6l1.6-1 2.2 2-1.2 2c-4.2-.4-8.4-4.6-8.8-8.8z" fill="var(--red)"/></svg>
    <span>470-555-0192</span>
  </div>
</section>

</body>
</html>
```